Inflatable Movie Screen company needs a Brochure Design for sales kit

We need a brochure as per attached sketch drawing which is to:
1)follow the sample layout
2) attached images must be used
3) to follow company corporate colors or suggest something professional and appropriate for the theme

Target Market(s)

Corporate and Community Clubs

Industry/Entity Type

Entertainment

Requirements
Must have
• Colors to be in line with corporate colors OR to suggest something appropriate.
Nice to have
• A unique concept
Should not have
• Too fanciful

```html
<!DOCTYPE html>
<html lang="en">
<head>
<meta charset="utf-8">
<title>Outdoor Movie Screenings – Sales Brochure</title>
<link href="https://fonts.googleapis.com/css2?family=PT+Sans:ital,wght@0,400;0,700;1,400;1,700&display=swap" rel="stylesheet">
<style>
:root{
  --navy:#0b3d8c;
  --blue:#1767bd;
  --mid:#2f86d3;
  --sky:#6cbcec;
  --pale:#d9eefb;
  --ink:#1b4b8a;
  --grey:#8c8c8c;
  --red:#d42027;
  --red-dark:#8e1116;
  --white:#ffffff;
}
*{margin:0;padding:0;box-sizing:border-box}
html,body{width:1200px;height:851px;overflow:hidden;background:var(--white)}
body{font-family:"PT Sans",Arial,sans-serif;font-style:italic;color:var(--white)}
.brochure{position:relative;width:1200px;height:851px;background:var(--white);overflow:hidden}

/* section bands */
.band-title{position:absolute;display:flex;align-items:center;font-size:33px;letter-spacing:.5px;text-transform:uppercase}
.why-band{left:0;top:31px;width:463px;height:76px;background:linear-gradient(90deg,var(--sky) 0%,var(--mid) 45%,var(--navy) 100%);padding-left:184px}
.film-strip{position:absolute;left:0;top:31px;width:150px;height:76px;background:linear-gradient(120deg,rgba(255,255,255,.55),rgba(255,255,255,.1))}
.expect-band{left:738px;top:31px;width:462px;height:73px;background:linear-gradient(90deg,var(--navy) 0%,var(--blue) 50%,var(--sky) 100%);padding-left:20px}

/* reasons */
.reason{position:absolute;left:0;width:735px;background:linear-gradient(90deg,var(--navy) 0%,var(--blue) 35%,var(--sky) 75%,rgba(255,255,255,0) 100%)}
.reason-1{top:129px;height:104px}
.reason-2{top:239px;height:92px}
.reason-3{top:347px;height:149px}
.reason-num{position:absolute;left:22px;font-size:90px;font-style:normal;line-height:1}
.reason-1 .reason-num{top:6px}
.reason-2 .reason-num{top:2px}
.reason-3 .reason-num{top:2px}
.reason-body{position:absolute;left:94px;top:14px;width:450px}
.reason-body h2{font-size:24px;font-weight:400;line-height:1;text-transform:uppercase}
.reason-body p{font-size:14.5px;line-height:1.15;text-align:justify}

/* photo placeholders */
.photo{position:absolute;border-radius:50%;border:5px solid var(--white);box-shadow:0 2px 6px rgba(0,0,0,.35)}
.photo-screen-day{left:492px;top:68px;width:146px;height:146px;background:radial-gradient(circle at 40% 40%,#e8eef4 0%,#5a7d9c 45%,#1d3557 100%)}
.photo-screen-trees{left:558px;top:261px;width:152px;height:152px;background:radial-gradient(circle at 55% 55%,#b8e0f2 0%,#4a7a3a 40%,#1c3a18 100%)}
.photo-screen-night{left:518px;top:581px;width:258px;height:258px;background:radial-gradient(circle at 55% 50%,#7fd0f5 0%,#2a6fa0 25%,#1a2230 65%,#0a0f18 100%)}

/* what to expect */
.expect-panel{position:absolute;left:700px;top:129px;width:500px;height:375px;background:linear-gradient(90deg,rgba(255,255,255,0) 0%,var(--sky) 30%,var(--blue) 75%,var(--navy) 100%)}
.expect-q{position:absolute;left:741px;top:152px;font-size:24px;text-transform:uppercase}
.expect-list{position:absolute;left:756px;top:198px;list-style:none;font-size:14.5px;line-height:1.35}
.expect-list li:nth-child(2){padding-left:3px}
.expect-list li:nth-child(3){padding-left:7px}
.expect-list li:nth-child(4){padding-left:11px}
.expect-list li:nth-child(5){padding-left:15px}
.cta-strip{position:absolute;left:765px;top:331px;width:435px;height:38px;background:linear-gradient(90deg,rgba(255,255,255,.95),var(--pale));color:var(--ink);font-weight:700;font-size:18px;padding:6px 0 0 14px}
.addons{position:absolute;left:792px;top:388px;font-size:19px;line-height:1.15}
.addon-list{position:absolute;left:772px;top:440px;list-style:none;font-size:15px;line-height:1.2}
.addon-list li{font-variant:small-caps}
.addon-list li:nth-child(1){padding-left:28px}
.addon-list li:nth-child(2){padding-left:20px}

/* clientele + book now */
.client-band{left:131px;top:518px;width:634px;height:70px;background:linear-gradient(90deg,var(--navy) 0%,var(--blue) 35%,var(--sky) 60%,var(--blue) 100%);padding-left:17px;font-size:25px}
.book-now{position:absolute;left:634px;top:539px;font-size:25px;text-transform:uppercase}
.movie{position:absolute;top:519px;width:74px;text-align:center}
.movie .poster{width:74px;height:74px;border-radius:50%;border:2px solid var(--white);box-shadow:0 1px 4px rgba(0,0,0,.3)}
.movie .label{display:block;margin-top:8px;font-size:12px;font-weight:700;font-style:normal;color:var(--blue);text-transform:uppercase;white-space:nowrap;margin-left:-10px;margin-right:-10px}
.movie-1{left:780px}.movie-1 .poster{background:radial-gradient(circle,#5ab3ea,#1d5fa8)}
.movie-2{left:865px}.movie-2 .poster{background:radial-gradient(circle,#e08a55,#3a7fa0)}
.movie-3{left:946px}.movie-3 .poster{background:radial-gradient(circle,#f0b060,#8a2a20)}
.movie-4{left:1031px}.movie-4 .poster{background:radial-gradient(circle,#e9f3ff,#5b8fd0)}
.movie-5{left:1112px}.movie-5 .poster{background:var(--white);border:1.5px solid #222;box-shadow:none}

/* client names */
.client{position:absolute;display:flex;align-items:center;gap:6px;font-weight:700;font-style:normal;font-size:18px;line-height:1;color:var(--grey);white-space:nowrap}
.client .dot{width:12px;height:12px;border-radius:50%;background:var(--grey)}
.client-norvale{left:27px;top:617px}
.client-kestra{left:196px;top:617px}
.client-halden{left:306px;top:617px}
.client-brightcast{left:27px;top:672px}
.client-skylane{left:142px;top:672px}
.client-pulsefit{left:226px;top:672px}
.client-orvix{left:318px;top:672px}

/* testimonial */
.quote{position:absolute;left:30px;top:728px;width:380px;font-size:19px;color:var(--ink);line-height:1.25}
.quote-by{position:absolute;left:162px;top:806px;font-size:19px;color:var(--ink)}

/* promotion */
.promo-band{position:absolute;left:759px;top:655px;width:441px;height:147px;background:linear-gradient(90deg,rgba(255,255,255,0) 0%,var(--mid) 18%,var(--blue) 60%,var(--navy) 100%)}
.promo-ribbon{position:absolute;left:762px;top:656px;width:112px;height:73px}
.promo-head{position:absolute;left:879px;top:663px;font-size:16px;text-transform:uppercase}
.promo-list{position:absolute;left:884px;top:700px;width:312px;list-style:none;font-size:15px;line-height:1.15}
.promo-list li{margin-bottom:10px}
</style>
</head>
<body>
<main class="brochure">

  <div class="band-title why-band">Why choose us?</div>
  <div class="film-strip" role="img" aria-label="Decorative film strip"></div>
  <div class="band-title expect-band">What to expect</div>

  <section class="reason reason-1">
    <span class="reason-num">1</span>
    <div class="reason-body">
      <h2>We are pioneers in this field</h2>
      <p>We have hosted outdoor movie screenings since 2008.<br>Till date, we have completed xx movie events.</p>
    </div>
  </section>
  <section class="reason reason-2">
    <span class="reason-num">2</span>
    <div class="reason-body">
      <h2>We are able to screen Starwell movies</h2>
      <p>We have partnered the only Frame Rights company that has exclusive rights to screen Starwell movies in DVD and other formats.</p>
    </div>
  </section>
  <section class="reason reason-3">
    <span class="reason-num">3</span>
    <div class="reason-body">
      <h2>We provide high quality,<br>weather-proof screens</h2>
      <p>Made from the same materials as cinema screens, our high quality PVC screen enhances images and movies viewers of an immense cinematic experience. If you are holding your events outdoors, don't fear for our screen is weather-proof.</p>
    </div>
  </section>

  <div class="expect-panel"></div>
  <div class="photo photo-screen-day" role="img" aria-label="Photo of an audience on a lawn watching an inflatable screen at dusk"></div>
  <div class="photo photo-screen-trees" role="img" aria-label="Photo of an inflatable screen among lit trees at night"></div>

  <p class="expect-q">Are you planning an event to...</p>
  <ul class="expect-list">
    <li>- improve staff welfare</li>
    <li>- launch a new product</li>
    <li>- build community spirit</li>
    <li>- create brand awareness</li>
    <li>- enhance team/corporate bonding</li>
  </ul>
  <div class="cta-strip">Let us organize a move-screening event for you!</div>
  <p class="addons">Your experience can be completed<br>with the following add-ons:</p>
  <ul class="addon-list">
    <li>A) popcorn</li>
    <li>B) catering</li>
    <li>C) themed / fringed-activities eg.</li>
  </ul>

  <div class="band-title client-band">Our clientele</div>
  <p class="book-now">Book now</p>

  <div class="movie movie-1"><div class="poster" role="img" aria-label="Movie poster artwork"></div><span class="label">Coral</span></div>
  <div class="movie movie-2"><div class="poster" role="img" aria-label="Movie poster artwork"></div><span class="label">Tidewave</span></div>
  <div class="movie movie-3"><div class="poster" role="img" aria-label="Movie poster artwork"></div><span class="label">Dr. Arcane</span></div>
  <div class="movie movie-4"><div class="poster" role="img" aria-label="Movie poster artwork"></div><span class="label">Snowbound</span></div>
  <div class="movie movie-5"><div class="poster"></div><span class="label">Sample</span></div>

  <span class="client client-norvale">Norvale</span>
  <span class="client client-kestra">Kestra</span>
  <span class="client client-halden">Halden</span>
  <span class="client client-brightcast"><span class="dot"></span>Brightcast</span>
  <span class="client client-skylane">SkyLane</span>
  <span class="client client-pulsefit">Pulsefit</span>
  <span class="client client-orvix">Orvix</span>

  <p class="quote">“Lorem ipsum dolor sit amet, consectetur adipiscing elit, sed do eiusmod tempor incididunt”</p>
  <p class="quote-by">- Marcus Tan, Company CEO</p>

  <div class="promo-band"></div>
  <div class="photo photo-screen-night" role="img" aria-label="Photo of a glowing outdoor screen among trees at night"></div>
  <svg class="promo-ribbon" viewBox="0 0 112 73" role="img" aria-label="Promotion ribbon">
    <polygon points="0,0 112,0 112,58 8,58 8,73 0,58" fill="var(--red)"/>
    <polygon points="0,58 8,58 8,73" fill="var(--red-dark)"/>
    <text x="56" y="37" text-anchor="middle" fill="#fff" font-family="PT Sans, Arial, sans-serif" font-size="20" textLength="98" lengthAdjust="spacingAndGlyphs">PROMOTION</text>
  </svg>
  <p class="promo-head">Sign up for our 1-year package now!</p>
  <ul class="promo-list">
    <li>· Get 8 movie screenings at 20% off</li>
    <li>· Your staff will also enjoy 20% off when they quote your corporate code to engage for their personal parties / events.</li>
  </ul>

</main>
</body>
</html>
```